Criação de Kit com 5 Layouts de Post para Redes Sociais (Facebook, Instagram e etc) para Construção & Engenharia
A empresa queria:
" Trabalho com a elaboração de projetos de engenharia em geral, sendo o maior foco e experiência os proj. de Prevenção e combate a incêndio, mas tbm na elaboração de projetos arquitetônico, estrutural, e de interiores. Regularização de obras junto a Prefeitura, Corpo de Bombeiros, Junta Ouromar, Vigilância Sanitária. Acompanhamento de Obras. "

```html
<!DOCTYPE html>
<html lang="pt-BR">
<head>
<meta charset="UTF-8">
<title>Post – Visita Técnica</title>
<link href="https://fonts.googleapis.com/css2?family=Montserrat:wght@400;500;700;800;900&family=Raleway:wght@400;500&display=swap" rel="stylesheet">
<style>
  :root{
    --ink:#2e3133;
    --gold:#b89a5c;
    --gold-light:#dcc79a;
    --gold-dark:#8e7440;
    --green:#1f2f2a;
    --paper:#f7f6f3;
    --white:#ffffff;
  }
  *{margin:0;padding:0;box-sizing:border-box}
  html,body{width:1200px;height:1200px;overflow:hidden;background:var(--white)}
  .post{position:relative;width:1200px;height:1200px;background:var(--paper);overflow:hidden;font-family:'Montserrat',sans-serif}
  .top-rule{position:absolute;left:0;top:0;width:100%;height:10px;background:linear-gradient(90deg,var(--gold-dark),var(--gold-light),var(--gold))}
  .hero-photo{position:absolute;left:430px;top:10px;width:770px;height:900px;
    background:linear-gradient(160deg,#c9ccd0 0%,#8f969c 35%,#5f676d 60%,#b9a27a 80%,#e6e1d8 100%);
    -webkit-mask-image:linear-gradient(90deg,transparent 0%,#000 35%);
    mask-image:linear-gradient(90deg,transparent 0%,#000 35%)}
  .headline{position:absolute;left:108px;top:78px;color:var(--ink);font-weight:900;font-size:74px;line-height:1.12;letter-spacing:1px;text-transform:uppercase}
  .cta-banner{position:absolute;left:0;top:408px;width:590px;height:158px;border-radius:0 80px 80px 0;
    background:linear-gradient(90deg,var(--gold-dark),var(--gold) 55%,var(--gold-light));
    display:flex;align-items:center;padding-left:108px}
  .cta-banner span{color:var(--white);font-weight:800;font-size:50px;line-height:1.12;text-transform:uppercase;letter-spacing:1px}
  .lead{position:absolute;left:108px;top:612px;width:700px;color:var(--ink);font-weight:800;font-size:44px;line-height:1.1}
  .accents{position:absolute;left:190px;top:810px}
  .divider{position:absolute;left:0;top:876px;width:1000px;height:3px;background:linear-gradient(90deg,transparent,var(--gold) 20%,var(--gold-light) 80%,transparent)}
  .footer{position:absolute;left:0;top:940px;width:1200px;height:210px}
  .footer-band{position:absolute;left:190px;top:14px;width:1010px;height:182px;background:var(--green)}
  .footer-edge{position:absolute;left:0;height:8px;width:1200px;background:linear-gradient(90deg,var(--gold-dark),var(--gold-light),var(--gold))}
  .footer-edge.top{top:0}.footer-edge.bottom{top:200px}
  .brand-block{position:absolute;left:0;top:8px;width:290px;height:192px;background:linear-gradient(135deg,#efe6d2,#cdb686);border-radius:0 90px 90px 0}
  .brand-mark{position:absolute;left:92px;top:52px;width:90px;height:90px;border:4px solid var(--green)}
  .brand{position:absolute;left:345px;top:68px;color:#e8e6e1}
  .brand-name{font-family:'Raleway',sans-serif;font-weight:400;font-size:48px;letter-spacing:6px;text-transform:uppercase}
  .brand-tagline{font-family:'Raleway',sans-serif;font-size:16px;letter-spacing:2.5px;text-transform:uppercase;margin-top:6px;color:#cfcac0}
  .contact{position:absolute;left:890px;top:58px;color:#e8e6e1}
  .contact-title{font-size:19px;font-weight:500;letter-spacing:1px;text-transform:uppercase;margin-bottom:10px}
  .contact-line{display:flex;align-items:center;gap:10px;font-weight:700}
  .contact-line.phone{font-size:26px;margin-bottom:8px}
  .contact-line.email{font-size:19px;font-weight:500}
</style>
</head>
<body>
<main class="post">
  <div class="top-rule"></div>
  <div class="hero-photo" role="img" aria-label="Engenheiro segurando capacete amarelo e plantas enroladas diante de prédios e uma avenida da cidade"></div>

  <h1 class="headline">Esta com<br>problemas<br>na sua obra?</h1>

  <div class="cta-banner"><span>Agende uma<br>visita técnica</span></div>

  <p class="lead">Podemos resolver todos os problemas realizando gerenciamento e acompanhamento.</p>

  <svg class="accents" width="140" height="80" viewBox="0 0 140 80">
    <rect x="10" y="40" width="26" height="26" transform="rotate(45 23 53)" fill="var(--gold-light)"/>
    <rect x="55" y="18" width="46" height="46" transform="rotate(45 78 41)" fill="var(--gold)"/>
  </svg>
  <div class="divider"></div>

  <footer class="footer">
    <div class="footer-band"></div>
    <div class="footer-edge top"></div>
    <div class="footer-edge bottom"></div>
    <div class="brand-block"><div class="brand-mark"></div></div>
    <div class="brand">
      <div class="brand-name">Lívia Marzano</div>
      <div class="brand-tagline">Projetando com qualidade e segurança</div>
    </div>
    <div class="contact">
      <div class="contact-title">Entre em contato</div>
      <div class="contact-line phone">
        <svg width="26" height="26" viewBox="0 0 24 24"><path fill="none" stroke="#e8e6e1" stroke-width="2" d="M6.6 3h3l1.5 4-2 1.3a11 11 0 0 0 6.6 6.6l1.3-2 4 1.5v3a2 2 0 0 1-2.2 2A17 17 0 0 1 4.6 5.2 2 2 0 0 1 6.6 3z"/></svg>
        (31) 90000 1234
      </div>
      <div class="contact-line email">
        <svg width="22" height="18" viewBox="0 0 22 18"><rect x="1" y="1" width="20" height="16" rx="2" fill="none" stroke="#e8e6e1" stroke-width="2"/><path d="M2 3l9 7 9-7" fill="none" stroke="#e8e6e1" stroke-width="2"/></svg>
        liviamarzano@email.com
      </div>
    </div>
  </footer>
</main>
</body>
</html>
```